Dietitian needs awesome business card

I need a contemporary design that's eye catching but professional.
My card is to given to doctors, specialists and patients alike.
I manage patients with chronic diseases
I have uploaded my logo and current business card, I would also like the other Certified Clinical Nutrition Adviser logo incorporated into the design

Target Market(s)

Doctors, specialists and patients

Industry/Entity Type

Healthcare

Contact Information for Business Card

www.brindlewaynutrition.com.au
Ph: 0427 514 903
Fax: 6482 7150
email: marcus.t.wellbeing@corvalmail.com
Space on the back of the card with: Appointment date, Appointment time and appointment location

Font styles to use
Serif

Colors
fbee3e
876aae
ffc214

Requirements
Must have
• My Logo
• Certified Clinical Nutrition Adviser Logo
• My 4 locations - Harrowfield Medical Centre, North Pellin Health, Kestwick Medical, Fernbrook Doctors Surgery
Nice to have
• I like the colours in my current business card

```html
<!DOCTYPE html>
<html lang="en">
<head>
<meta charset="utf-8">
<title>Brindleway Nutrition &amp; Dietetics — Business Card</title>
<link rel="stylesheet" href="https://fonts.googleapis.com/css2?family=Marcellus&family=Lora:wght@400;500&display=swap">
<style>
  :root {
    --bg: #3b3c3e;
    --card: #fbfbfb;
    --blue: #1f8ad2;
    --blue-deep: #1a5ea8;
    --green: #8cc63f;
    --green-deep: #2ca14a;
    --yellow: #e4e21f;
    --orange: #f08a3c;
    --grey: #5d6066;
    --line: #a9acb2;
  }
  * { box-sizing: border-box; margin: 0; padding: 0; }
  html, body { width: 1200px; height: 900px; overflow: hidden; }
  body {
    background: var(--bg);
    font-family: "Marcellus", "Lora", serif;
    position: relative;
  }
  .card {
    position: absolute;
    top: 140px;
    width: 380px;
    height: 620px;
    background: var(--card);
    box-shadow: 0 18px 40px rgba(0,0,0,.45);
    overflow: hidden;
  }
  .card--front { left: 170px; }
  .card--back  { left: 650px; }

  .edge { position: absolute; top: 0; bottom: 0; width: 14px; }
  .card--front .edge--left {
    left: 0;
    background: linear-gradient(to bottom, var(--blue-deep) 0%, var(--blue) 50%, var(--yellow) 58%, var(--green) 75%, var(--green-deep) 100%);
  }
  .card--back .edge--left {
    left: 0;
    background: linear-gradient(to bottom, var(--blue) 0%, var(--blue-deep) 100%);
  }
  .card--back .edge--right {
    right: 0;
    background: linear-gradient(to bottom, var(--green-deep) 0%, var(--green) 30%, var(--yellow) 50%, var(--blue) 75%, var(--blue-deep) 100%);
  }

  /* Front */
  .credential-badge {
    position: absolute;
    top: 26px; right: 26px;
    width: 112px; height: 56px;
  }
  .brand {
    position: absolute;
    top: 240px; left: 40px; right: 20px;
    display: flex; align-items: center; gap: 14px;
  }
  .brand__mark { width: 70px; height: 70px; border-radius: 50%; background: var(--blue); flex: none; }
  .brand__name {
    color: var(--blue-deep);
    font-family: "Marcellus", serif;
    font-weight: 400;
    line-height: 1.05;
  }
  .brand__name .primary { display: block; font-size: 38px; }
  .brand__name .secondary { display: block; font-size: 16px; margin-top: 4px; }

  .person {
    position: absolute;
    top: 420px; left: 40px;
    color: var(--blue);
    font-size: 25px;
    letter-spacing: 1px;
    text-transform: uppercase;
  }
  .contacts {
    position: absolute;
    top: 468px; left: 40px;
    list-style: none;
  }
  .contacts li {
    display: flex; align-items: center; gap: 10px;
    height: 30px;
    color: var(--grey);
    font-family: "Lora", serif;
    font-size: 16px;
  }
  .contacts li.small { font-size: 14px; }
  .contact-icon { width: 22px; height: 22px; flex: none; }

  /* Back */
  .appointment {
    position: absolute;
    top: 40px; left: 44px; right: 36px;
  }
  .appointment__title {
    color: var(--blue);
    font-size: 32px;
    letter-spacing: 2px;
    font-weight: 400;
    margin-bottom: 26px;
  }
  .field {
    display: flex; align-items: flex-end;
    height: 42px;
    color: var(--grey);
    font-family: "Lora", serif;
    font-size: 17px;
  }
  .field__line {
    flex: 1;
    margin-left: 8px;
    border-bottom: 2px dotted var(--line);
    height: 1px;
    margin-bottom: 5px;
  }
  .locations {
    position: absolute;
    top: 392px; left: 44px; right: 30px;
  }
  .locations__title {
    color: var(--green);
    font-size: 22px;
    letter-spacing: 1px;
    font-weight: 400;
    margin-bottom: 16px;
  }
  .locations ul { list-style: none; }
  .locations li {
    display: flex; align-items: center; gap: 12px;
    height: 34px;
    color: var(--blue-deep);
    font-family: "Lora", serif;
    font-size: 17px;
  }
  .checkbox {
    width: 18px; height: 18px;
    border: 1.5px solid #55585e;
    flex: none;
  }
</style>
</head>
<body>

  <section class="card card--front" aria-label="Business card front">
    <div class="edge edge--left"></div>

    <svg class="credential-badge" viewBox="0 0 112 56" role="img" aria-label="Certified Clinical Nutrition Adviser badge">
      <rect width="112" height="56" fill="#f08a3c"/>
      <circle cx="84" cy="28" r="16" fill="#ffffff"/>
    </svg>

    <div class="brand">
      <span class="brand__mark"></span>
      <div class="brand__name">
        <span class="primary">Brindleway</span>
        <span class="secondary">Nutrition &amp; Dietetics</span>
      </div>
    </div>

    <h1 class="person">Marcus Tellwright</h1>

    <ul class="contacts">
      <li>
        <svg class="contact-icon" viewBox="0 0 22 22" aria-hidden="true">
          <circle cx="11" cy="11" r="11" fill="#1f8ad2"/>
          <rect x="6" y="9" width="10" height="6" rx="1" fill="#fff"/>
          <rect x="8" y="5.5" width="6" height="3.5" fill="#fff"/>
          <rect x="8" y="13" width="6" height="3.5" fill="#1f8ad2" stroke="#fff" stroke-width="1"/>
        </svg>
        6482 7150
      </li>
      <li>
        <svg class="contact-icon" viewBox="0 0 22 22" aria-hidden="true">
          <circle cx="11" cy="11" r="11" fill="#1f8ad2"/>
          <path d="M7.5 6.5c1-.8 1.8-.5 2.3.5l.6 1.3c.3.6 0 1.1-.5 1.5l-.5.4c.6 1.3 1.6 2.3 2.9 2.9l.4-.5c.4-.5.9-.8 1.5-.5l1.3.6c1 .5 1.3 1.3.5 2.3-1 1.2-2.6 1.3-4.5.1-1.6-1-3-2.4-4-4-1.2-1.9-1.1-3.5.1-4.5z" fill="#fff"/>
        </svg>
        0427 514 903
      </li>
      <li class="small">
        <svg class="contact-icon" viewBox="0 0 22 22" aria-hidden="true">
          <circle cx="11" cy="11" r="11" fill="#1f8ad2"/>
          <rect x="5.5" y="7" width="11" height="8" rx="1" fill="#fff"/>
          <path d="M5.8 7.5 11 11.5l5.2-4" fill="none" stroke="#1f8ad2" stroke-width="1.2"/>
        </svg>
        marcus.t.wellbeing@corvalmail.com
      </li>
      <li class="small">
        <svg class="contact-icon" viewBox="0 0 22 22" aria-hidden="true">
          <circle cx="11" cy="11" r="11" fill="#1f8ad2"/>
          <circle cx="11" cy="11" r="5.5" fill="none" stroke="#fff" stroke-width="1.2"/>
          <ellipse cx="11" cy="11" rx="2.3" ry="5.5" fill="none" stroke="#fff" stroke-width="1"/>
          <path d="M5.5 11h11" stroke="#fff" stroke-width="1"/>
        </svg>
        www.brindlewaynutrition.com.au
      </li>
    </ul>
  </section>

  <section class="card card--back" aria-label="Business card back">
    <div class="edge edge--left"></div>
    <div class="edge edge--right"></div>

    <div class="appointment">
      <h2 class="appointment__title">APPOINTMENT</h2>
      <div class="field">Date:<span class="field__line"></span></div>
      <div class="field">Time:<span class="field__line"></span></div>
      <div class="field">Date:<span class="field__line"></span></div>
      <div class="field">Time:<span class="field__line"></span></div>
      <div class="field">Date:<span class="field__line"></span></div>
      <div class="field">Time:<span class="field__line"></span></div>
    </div>

    <div class="locations">
      <h2 class="locations__title">APPOINTMENT LOCATION</h2>
      <ul>
        <li><span class="checkbox"></span>North Pellin Health</li>
        <li><span class="checkbox"></span>Kestwick Medical</li>
        <li><span class="checkbox"></span>Harrowfield Medical Centre</li>
        <li><span class="checkbox"></span>Fernbrook Doctors Surgery</li>
      </ul>
    </div>
  </section>

</body>
</html>
```